Create Brisk Lesson Studio a card design that will stick in the mind of prospects.

Brisk Lesson Studio specialises designs and produces training video, animation, illustration and text.

We need a card design that oozes class and leaves the prospect brimming with confidence.

The design will feature the Brisk Lesson Studio all black logo (uploaded). The design may also use the shade of orange from the orange version of the logo (uploaded). Note, just the color is to be used e.g. for the back of the card, not the orange logo itself.

The Brisk brand is about authenticity, quality, maturity and assurance. We are a safe buy when it comes to the prospects next project.

Target Market(s)

The primary target is training managers or others who are responsible for choosing to hire companies to produce their training media e.g. video. This will usually be a large spend so they need to have confidence.

Industry/Entity Type

Training

Contact Information for Business Card

FRONT:

Brisk Lesson Studio
Phone: 03 5172 4039
1st Floor, 418 Kellerby Road
Mt Ferncombe
VIC 3862
Australia
www.brisklesson.com.au

Lionel Petch
Founder and Lead Consultant
mobile: +61 3 0462 735 218
email: lionel@brisklesson.com.au

BACK:
Specialising in design and production of training:

video
animation
illustration
text

for delivery via internet, intranet and/or LMS.

Number of Pages Required

4 page

Font styles to use
Sans Serif

Requirements
Must have
• The black logo uploaded with the brief.
Nice to have
• The inclusion of the shade of orange found in the orange logo also uploaded with the brief. One example would be having the back of the card in this orange and using a white font for the text. But I want the designer to work this out.
Should not have
• No colours other than black and the orange included in the uploaded orange logo.

```html
<!DOCTYPE html>
<html lang="en">
<head>
<meta charset="utf-8">
<title>Brisk Lesson Studio – Business Card</title>
<link rel="stylesheet" href="https://fonts.googleapis.com/css2?family=Exo+2:wght@400;700&display=swap">
<style>
  :root {
    --backdrop: #e6e6e6;
    --card: #ffffff;
    --ink: #111111;
    --ornament: #8a8a8a;
    --rule: #1a1a1a;
  }
  * { margin: 0; padding: 0; box-sizing: border-box; }
  html, body { width: 1200px; height: 848px; overflow: hidden; }
  body {
    background: var(--backdrop);
    font-family: "Exo 2", Arial, sans-serif;
    color: var(--ink);
    position: relative;
  }
  .card {
    position: absolute;
    top: 154px;
    width: 350px;
    height: 540px;
    background: var(--card);
    box-shadow: 0 6px 18px rgba(0,0,0,0.12);
  }
  .card--front { left: 220px; }
  .card--back { left: 630px; }

  .ornament {
    position: absolute;
    width: 48px;
    height: 36px;
    background: var(--ornament);
    opacity: 0.45;
  }
  .ornament--tl { top: 16px; left: 16px; }
  .ornament--tr { top: 16px; right: 16px; }
  .ornament--bl { bottom: 16px; left: 16px; }
  .ornament--br { bottom: 16px; right: 16px; }

  .identity { position: absolute; top: 128px; left: 60px; right: 24px; }
  .identity__name { font-size: 30px; line-height: 1; font-weight: 400; }
  .identity__name strong { font-weight: 700; }
  .identity__role { font-size: 15px; margin-top: 4px; }

  .contact-list { position: absolute; top: 212px; left: 60px; right: 20px; list-style: none; }
  .contact-list__item {
    display: flex;
    align-items: center;
    gap: 14px;
    margin-bottom: 22px;
  }
  .contact-list__icon { width: 22px; height: 22px; flex: none; }
  .contact-list__text { font-size: 12.5px; line-height: 1.35; }

  .brand {
    position: absolute;
    top: 96px;
    left: 40px;
    right: 40px;
    height: 180px;
  }
  .brand__rule {
    position: absolute;
    left: 0; right: 0;
    height: 1.5px;
    background: var(--rule);
  }
  .brand__rule--top { top: 36px; }
  .brand__rule--bottom { bottom: 36px; }
  .brand__name {
    position: absolute;
    top: 50%;
    left: 0; right: 0;
    transform: translateY(-50%);
    text-align: center;
    font-size: 64px;
    font-weight: 700;
    letter-spacing: 1px;
  }

  .services {
    position: absolute;
    top: 300px;
    left: 40px;
    right: 40px;
    text-align: center;
    font-size: 13px;
    line-height: 1.5;
  }
  .services__list {
    list-style: none;
    margin: 10px 0;
    font-weight: 700;
    font-size: 14px;
  }
</style>
</head>
<body>

  <section class="card card--front" aria-label="Card front">
    <div class="ornament ornament--tl" role="img" aria-label="Flourish corner ornament"></div>
    <div class="ornament ornament--tr" role="img" aria-label="Flourish corner ornament"></div>
    <div class="ornament ornament--bl" role="img" aria-label="Flourish corner ornament"></div>

    <div class="identity">
      <p class="identity__name"><strong>Lionel</strong> Petch</p>
      <p class="identity__role">Founder and Lead Consultant</p>
    </div>

    <ul class="contact-list">
      <li class="contact-list__item">
        <svg class="contact-list__icon" viewBox="0 0 22 22" aria-hidden="true">
          <rect width="22" height="22" rx="3" fill="#111"/>
          <path d="M8 6 l2 0 l1 3 l-1.5 1 a6 6 0 0 0 2.5 2.5 l1 -1.5 l3 1 l0 2 a1.5 1.5 0 0 1 -1.5 1.5 a9 9 0 0 1 -8 -8 a1.5 1.5 0 0 1 1.5 -1.5z" fill="#fff"/>
        </svg>
        <p class="contact-list__text">mobile: +61 3 0462 735 218<br>phone: 03 5172 4039</p>
      </li>
      <li class="contact-list__item">
        <svg class="contact-list__icon" viewBox="0 0 22 22" aria-hidden="true">
          <rect width="22" height="22" rx="3" fill="#111"/>
          <circle cx="11" cy="11" r="5.5" fill="none" stroke="#fff" stroke-width="1.5"/>
          <circle cx="11" cy="11" r="2.2" fill="none" stroke="#fff" stroke-width="1.5"/>
        </svg>
        <p class="contact-list__text">lionel@brisklesson.com.au<br>www.brisklesson.com.au</p>
      </li>
      <li class="contact-list__item">
        <svg class="contact-list__icon" viewBox="0 0 22 22" aria-hidden="true">
          <rect width="22" height="22" rx="3" fill="#111"/>
          <path d="M11 5 a4.5 4.5 0 0 1 4.5 4.5 c0 3 -4.5 7.5 -4.5 7.5 s-4.5 -4.5 -4.5 -7.5 a4.5 4.5 0 0 1 4.5 -4.5z" fill="#fff"/>
          <circle cx="11" cy="9.5" r="1.6" fill="#111"/>
        </svg>
        <p class="contact-list__text">Brisk Lesson Studio<br>1st Floor, 418 Kellerby Road<br>Mt Ferncombe VIC 3862<br>Australia</p>
      </li>
    </ul>
  </section>

  <section class="card card--back" aria-label="Card back">
    <div class="ornament ornament--tl" role="img" aria-label="Flourish corner ornament"></div>
    <div class="ornament ornament--tr" role="img" aria-label="Flourish corner ornament"></div>
    <div class="ornament ornament--bl" role="img" aria-label="Flourish corner ornament"></div>
    <div class="ornament ornament--br" role="img" aria-label="Flourish corner ornament"></div>

    <div class="brand">
      <span class="brand__rule brand__rule--top"></span>
      <p class="brand__name">Brisk</p>
      <span class="brand__rule brand__rule--bottom"></span>
    </div>

    <div class="services">
      <p>Specialising in design and production of training:</p>
      <ul class="services__list">
        <li>video</li>
        <li>animation</li>
        <li>illustration</li>
        <li>text</li>
      </ul>
      <p>for delivery via internet, intranet and/or LMS.</p>
    </div>
  </section>

</body>
</html>
```